Book Cover for Willow Kindred Notes from the Meadow

We have written a book that brings together Notes from the Meadow from a variety of women's voices.
We developed a draft book cover that we like using Canva (attached below). We'd love a book cover that is similar to this image, but looks more professional.
Following are the themes we’d like to depict in the book cover, and in parentheses, how they are represented in the current cover:
1. Divinely feminine (overall cover)
2. Currents of enlightenment (the swirls of light carrying the butterfly)
3. Diversity (a myriad of colors)
4. The solo journey into the unknown (the single butterfly’s flight)
5. Buoyancy and joy (again, the dancing colors and floating butterfly)
6. Boldly feminine (the blue butterfly, set against brush strokes of light)
7. Homage to a dear friend (she loved blue butterflies, the cosmos - this butterfly has hints of the cosmos in her wings, and painting - this background has brush strokes of light).
Book Title, Subtitle, and Editor:
Willow Kindred
Notes from the Meadow
Edited by Mirela Tove
Thank you very much for considering this project!
People who are interested in Women and Spirituality

```html
<!DOCTYPE html>
<html lang="en">
<head>
<meta charset="utf-8">
<title>Notes from the Meadow — Willow Kindred</title>
<link href="https://fonts.googleapis.com/css2?family=Cinzel:wght@400;500&family=Dancing+Script:wght@500&display=swap" rel="stylesheet">
<style>
  :root {
    --paper: #e6ecea;
    --mist: #d4e6e6;
    --aqua: #9fd3d6;
    --blush: #f1e3dc;
    --navy: #0e1d8a;
    --teal: #3b7478;
    --wing-deep: #1a3f9a;
    --wing-bright: #2fb8d2;
    --wing-ink: #142a78;
    --berry: #e0202a;
  }
  html, body {
    margin: 0;
    padding: 0;
    overflow: hidden;
  }
  .cover {
    position: relative;
    width: 752px;
    height: 1200px;
    overflow: hidden;
    background:
      radial-gradient(ellipse 180px 260px at 60px 520px, rgba(159,211,214,0.75), transparent 70%),
      radial-gradient(ellipse 220px 160px at 360px 130px, rgba(159,211,214,0.55), transparent 70%),
      radial-gradient(ellipse 260px 200px at 120px 820px, rgba(180,220,222,0.6), transparent 70%),
      radial-gradient(ellipse 200px 240px at 700px 120px, rgba(241,227,220,0.8), transparent 70%),
      radial-gradient(ellipse 300px 200px at 560px 1000px, rgba(212,230,230,0.7), transparent 70%),
      linear-gradient(170deg, var(--mist) 0%, var(--paper) 55%, #e9ecea 100%);
  }
  .title {
    position: absolute;
    left: 54px;
    right: 46px;
    top: 96px;
    margin: 0;
    color: var(--navy);
    font-weight: 400;
  }
  .title-line {
    display: flex;
    align-items: baseline;
    justify-content: space-between;
    font-family: "Cinzel", serif;
    line-height: 1;
  }
  .title-line--first {
    font-size: 88px;
    justify-content: flex-start;
    gap: 0;
  }
  .title-line--first .caps {
    letter-spacing: 0.42em;
  }
  .title-line--second {
    font-size: 70px;
    margin-top: 30px;
    letter-spacing: 0.38em;
    padding-left: 2px;
  }
  .script {
    font-family: "Dancing Script", cursive;
    font-size: 54px;
    letter-spacing: 0;
    margin-left: -14px;
  }
  .butterfly {
    position: absolute;
    left: 244px;
    top: 398px;
    width: 396px;
    height: 455px;
    border-radius: 58% 42% 46% 54% / 40% 30% 70% 60%;
    background:
      radial-gradient(ellipse 120px 160px at 120px 190px, var(--wing-bright), transparent 75%),
      linear-gradient(200deg, var(--wing-ink) 0%, var(--wing-deep) 45%, #2478b8 75%, var(--wing-ink) 100%);
    opacity: 0.92;
  }
  .accent-dot {
    position: absolute;
    left: 107px;
    top: 1152px;
    width: 18px;
    height: 18px;
    border-radius: 50%;
    background: var(--berry);
  }
  .credits {
    position: absolute;
    left: 0;
    right: 0;
    top: 1030px;
    color: var(--teal);
    font-family: "Cinzel", serif;
    text-align: center;
  }
  .editor {
    margin: 0;
    font-size: 29px;
    font-weight: 500;
    letter-spacing: 0.22em;
    padding-left: 40px;
  }
  .publisher {
    margin: 12px 0 0;
    font-size: 52px;
    font-weight: 400;
    letter-spacing: 0.2em;
    padding-left: 54px;
  }
</style>
</head>
<body>
  <main class="cover">
    <h1 class="title">
      <span class="title-line title-line--first"><span class="caps">NOTES</span><span class="script">from the</span></span>
      <span class="title-line title-line--second"><span>M</span><span>E</span><span>A</span><span>D</span><span>O</span><span>W</span></span>
    </h1>

    <div class="butterfly" role="img" aria-label="A single blue butterfly with cosmic turquoise-speckled wings in flight"></div>

    <span class="accent-dot"></span>

    <footer class="credits">
      <p class="editor">EDITED BY MIRELA TOVE</p>
      <p class="publisher">WILLOW KINDRED</p>
    </footer>
  </main>
</body>
</html>
```